Business card for our start up Automotive Shop

Clean business card design for our new automotive shop Brightline Motor Works. This card will be the template for all of our staff member including technicians and service advisors.

Brightline Motor Works is an automotive service shop catering to US domestic and asian import vehicles. We are a service and maintenance full service facility. Our aim is to provide the best quality workmanship and the best customer service experience in our industry.

Our target market are young professionals to people with families. We are not targeting a younger audience or the car modification scene. The card should be appealing to women of the 30+ age demographic.

We are a shop of younger professionals instead of an older crowd. The card design should reflect as such.

Target Market(s)

30+ Female demographic and 30+ male.

Industry/Entity Type

Automotive

Contact Information for Business Card

Must be clean and appealing to clients. Large enough and easy to read print.

Font styles to use
Sans Serif

Colors
f78f20
ffffff
b2b2b2
dddddd

Requirements
Must have
• Address, website and phone number
• 42-15 58th Ave
• Cedar Hollow NY 11462
• (718) 402-3917
• brightlinemotorworks.com
• There must be an area to add a Name and e-mail address for personalization purposes.
Nice to have
• Back of the card should have website.
• I would also like to incorporate yelp, google+, Facebook, and instagram widgets. Will add the exact pages but everything can be @ or / brightlinemotorworks
• That can be added on the back of the card.

```html
<!DOCTYPE html>
<html lang="en">
<head>
<meta charset="utf-8">
<title>Brightline Motor Works – Business Card</title>
<link rel="stylesheet" href="https://fonts.googleapis.com/css2?family=Montserrat:wght@500;600&family=Lato:wght@400;700&display=swap">
<style>
  :root{
    --orange:#f78f20;
    --orange-deep:#e8601f;
    --orange-soft:#f9b25e;
    --paper:#f4f4f2;
    --light:#dddddd;
    --grey:#b2b2b2;
    --ink:#2d2d2d;
    --backdrop:#d6d6d6;
  }
  *{margin:0;padding:0;box-sizing:border-box}
  html,body{width:1200px;height:899px;overflow:hidden}
  body{background:var(--backdrop);font-family:"Lato",sans-serif;color:var(--ink);position:relative}

  .card{position:absolute;left:290px;width:620px;height:354px;background:var(--paper);
        overflow:hidden;box-shadow:0 6px 18px rgba(0,0,0,.18)}
  .card--front{top:52px}
  .card--back{top:480px}
  .card svg.shapes{position:absolute;inset:0}

  /* front */
  .front-rays{position:absolute;left:0;top:0;width:250px;height:354px;
    background:linear-gradient(135deg,var(--orange-soft),var(--orange) 45%,var(--orange-deep));
    clip-path:polygon(0 18%,100% 48%,40% 100%,0 100%)}
  .brand{position:absolute;display:flex;align-items:center;gap:12px}
  .brand__mark{border-radius:50%;background:var(--orange);flex:none}
  .brand__name{font-family:"Montserrat",sans-serif;font-weight:600;color:var(--orange);
    text-transform:uppercase;letter-spacing:.06em;white-space:nowrap;line-height:1.1}
  .brand__line{display:block}
  .card--front .brand{left:262px;top:112px;gap:14px}
  .card--front .brand__mark{width:64px;height:64px}
  .card--front .brand__name{font-size:27px}

  /* back */
  .card--back .brand{left:62px;top:38px;gap:9px}
  .card--back .brand__mark{width:34px;height:34px}
  .card--back .brand__name{font-size:15px}

  .person{position:absolute;left:36px;top:168px;font-family:"Montserrat",sans-serif}
  .person__name{font-size:24px;font-weight:500;color:#fff;letter-spacing:.02em}
  .person__name em{font-style:normal;color:var(--orange)}
  .person__role{font-size:19px;color:#fff;margin-top:4px;padding-left:8px}
  .person__role span{color:var(--orange)}

  .contact{position:absolute;left:372px;top:62px;list-style:none}
  .contact__row{display:flex;align-items:center;height:40px;margin-bottom:10px}
  .contact__icon{width:40px;height:40px;background:var(--ink);display:flex;align-items:center;justify-content:center;flex:none}
  .contact__text{height:40px;width:204px;background:var(--paper);display:flex;flex-direction:column;justify-content:center;
    padding-left:12px;font-size:15px;line-height:1.15}
  .contact__text--small{font-size:12.5px}

  .follow{position:absolute;left:20px;right:20px;top:286px;height:40px;background:var(--light);
    display:flex;align-items:center;padding:0 16px;font-size:14px}
  .follow__label{text-transform:uppercase;color:#555;letter-spacing:.02em;margin-right:auto}
  .follow__badge{width:24px;height:24px;background:#555;border-radius:5px;margin-right:16px}
  .follow__handle{font-size:15px;color:#444;margin-left:6px}
  .card__edge{position:absolute;left:0;right:0;bottom:0;height:9px;background:var(--ink)}
</style>
</head>
<body>

<section class="card card--front" aria-label="Front of business card">
  <div class="front-rays" role="img" aria-label="Orange sunburst ray graphic"></div>
  <div class="brand">
    <span class="brand__mark"></span>
    <span class="brand__name"><span class="brand__line">Brightline</span><span class="brand__line">Motor Works</span></span>
  </div>
</section>

<section class="card card--back" aria-label="Back of business card">
  <svg class="shapes" width="620" height="354" viewBox="0 0 620 354" aria-hidden="true">
    <defs>
      <linearGradient id="band" x1="0" y1="0" x2="1" y2="1">
        <stop offset="0" stop-color="#f9a64a"/>
        <stop offset="1" stop-color="#ef7a1e"/>
      </linearGradient>
    </defs>
    <polygon points="0,22 70,22 24,240 0,240" fill="url(#band)"/>
    <polygon points="44,150 318,150 280,252 0,252 0,200" fill="#2d2d2d"/>
    <polygon points="0,252 280,252 276,260 0,260" fill="#f78f20"/>
    <polygon points="340,10 620,10 620,272 262,272" fill="url(#band)"/>
    <polygon points="360,10 620,10 620,50 352,50" fill="#f9b25e" opacity=".45"/>
  </svg>

  <div class="brand">
    <span class="brand__mark"></span>
    <span class="brand__name"><span class="brand__line">Brightline</span><span class="brand__line">Motor Works</span></span>
  </div>

  <div class="person">
    <p class="person__name">YOUR <em>NAME</em></p>
    <p class="person__role"><span>|</span> Designation <span>|</span></p>
  </div>

  <ul class="contact">
    <li class="contact__row">
      <span class="contact__icon">
        <svg width="22" height="22" viewBox="0 0 24 24" fill="none" stroke="#fff" stroke-width="1.8"><circle cx="12" cy="12" r="10.5"/><path d="M8.5 7c-.8.8-.6 3 1.4 5.3s4.2 3 5 2.2l.9-.9-1.8-1.6-1 .8c-.8-.3-2.2-1.700-2.5-2.5l.8-1L9.7 6z" fill="#fff" stroke="none"/></svg>
      </span>
      <span class="contact__text">(718) 402-3917</span>
    </li>
    <li class="contact__row">
      <span class="contact__icon">
        <svg width="22" height="22" viewBox="0 0 24 24" fill="none" stroke="#fff" stroke-width="1.6"><circle cx="12" cy="12" r="10"/><ellipse cx="12" cy="12" rx="4.5" ry="10"/><path d="M2 12h20M4 7h16M4 17h16"/></svg>
      </span>
      <span class="contact__text">brightlinemotorworks.com</span>
    </li>
    <li class="contact__row">
      <span class="contact__icon">
        <svg width="22" height="22" viewBox="0 0 24 24" fill="none" stroke="#fff" stroke-width="1.8"><circle cx="12" cy="12" r="10.5"/><path d="M12 18.5s-4.5-4.6-4.5-7.8a4.5 4.5 0 0 1 9 0c0 3.2-4.5 7.8-4.5 7.8z"/><circle cx="12" cy="10.6" r="1.5"/></svg>
      </span>
      <span class="contact__text contact__text--small"><span>42-15 58th Ave</span><span>Cedar Hollow NY 11462</span></span>
    </li>
  </ul>

  <div class="follow">
    <span class="follow__label">Follow us at</span>
    <span class="follow__badge"></span>
    <span class="follow__badge"></span>
    <span class="follow__badge"></span>
    <span class="follow__badge"></span>
    <span class="follow__handle">@brightlinemotorworks</span>
  </div>
  <div class="card__edge"></div>
</section>

</body>
</html>
```